Your 'not so average' farmers. We are farmers and entrepreneurs trying to connect the great divide.

KTB (Brosmere Holdings Inc) is a family owned farm (in our 3rd generation). We grow vegetables (corn, soy, potatoes, snap beans) but we also invest in and grow businesses. These other businesses can be non-farming related businesses. We are family oriented, environmentally concise, and active in our small community. We need a business card to hand out to our fellow farmers, businesses we would like to partner with and invest in, and community members. So, we need a card with a natural, 'tenders of the land' feel for the farmers but no overly so that we seem centered on farming for the other businesses. We would like it to have our Company info (name, number, email, phone, fax) then Personal info for us five who run the joint (Name, phone, email). So we will order 100 cards for each 5 who work at KTB (500total) that is professional, not boring or hokey, but catching and unique.
Target Market(s)
Farmers, Business Owners, Investors, Community Members
Industry/Entity Type
Farming
Contact Information for Business Card
Office info on one side:
Brosmere Holdings Inc.
1187 Larkin Rd.
Pell Hollow, WI 54872
Office: (608) 555-0417
Fax: (608) 555-0283
brosmereoffice@quillpost.example
Personal Info for the 5 who run KTB. Everybody will have their own personal info on their cards(maybe on the other side):
Name
Mobile
Email
Look and feel

```html
<!DOCTYPE html>
<html lang="en">
<head>
<meta charset="utf-8">
<title>Brosmere Holdings Inc. – Business Card</title>
<link rel="stylesheet" href="https://fonts.googleapis.com/css2?family=Josefin+Sans:wght@300;400&display=swap">
<style>
  :root {
    --page: #d9d9d9;
    --ink: #2e2e2e;
    --ink-soft: #4a4a4a;
    --white: #ffffff;
    --sky-top: #3f6db5;
    --sky-low: #a9c3e0;
    --field-far: #6d9a3a;
    --field-near: #5f9a2a;
    --field-gold: #c8a04a;
    --panel-green: rgba(128, 196, 72, 0.88);
    --panel-line: rgba(255, 255, 255, 0.18);
    --veil: rgba(255, 255, 255, 0.62);
    --icon: #6b6b6b;
    --dusk-top: #5a7fae;
    --dusk-mid: #c9d3dc;
    --dusk-ground: #6f5a2c;
  }
  * { box-sizing: border-box; margin: 0; padding: 0; }
  html, body { width: 1200px; height: 900px; overflow: hidden; }
  body {
    background: var(--page);
    font-family: "Josefin Sans", sans-serif;
    color: var(--ink);
    position: relative;
  }
  .card {
    position: absolute;
    left: 250px;
    width: 700px;
    height: 400px;
    overflow: hidden;
    box-shadow: 0 6px 18px rgba(0,0,0,0.25);
  }
  .card--front { top: 35px; }
  .card--back { top: 465px; }

  /* Front */
  .front-photo {
    position: absolute; inset: 0;
    background: linear-gradient(180deg,
      var(--sky-top) 0%, var(--sky-low) 40%,
      var(--field-far) 44%, var(--field-gold) 54%,
      var(--field-near) 62%, #4f8a22 100%);
  }
  .front-band {
    position: absolute; left: 0; right: 0; top: 88px; height: 90px;
    background: var(--veil);
    text-align: center;
  }
  .front-name {
    font-size: 34px; font-weight: 300; letter-spacing: 2px;
    margin-top: 16px; color: var(--ink);
  }
  .front-contact {
    font-size: 18px; font-weight: 300; letter-spacing: 0.5px;
    margin-top: 6px; color: var(--ink-soft);
  }
  .front-company {
    position: absolute; left: 0; right: 0; top: 186px;
    text-align: center; color: var(--white);
    font-size: 22px; font-weight: 300; letter-spacing: 3px;
    text-transform: uppercase;
  }

  /* Back */
  .back-photo-left {
    position: absolute; left: 0; top: 0; bottom: 0; width: 150px;
    background: linear-gradient(180deg, var(--dusk-top) 0%, var(--dusk-mid) 35%, var(--dusk-ground) 55%, #4b5a24 100%);
  }
  .back-photo-right {
    position: absolute; right: 0; top: 0; bottom: 0; width: 190px;
    background: linear-gradient(180deg, #8aa4c8 0%, #c8d4e0 45%, #9a8a4a 60%, #6a5a26 100%);
  }
  .icon-column {
    position: absolute; left: 150px; top: 0; bottom: 0; width: 85px;
    background: rgba(255,255,255,0.55);
  }
  .icon { position: absolute; left: 25px; width: 34px; height: 30px; fill: var(--icon); }
  .icon--phone { top: 46px; }
  .icon--mail { top: 130px; }
  .icon--home { top: 214px; }
  .info-panel {
    position: absolute; left: 235px; top: 0; bottom: 0; width: 275px;
    background: var(--panel-green);
  }
  .info-row {
    position: absolute; left: 0; right: 0; height: 1px; background: var(--panel-line);
  }
  .info-panel-wide {
    position: absolute; left: 235px; top: 0; bottom: 0; right: 190px;
    background: var(--panel-green);
    padding: 20px 0 0 18px;
  }
  .company-title {
    font-size: 17px; letter-spacing: 2.5px; text-transform: uppercase;
    font-weight: 400; color: var(--ink);
  }
  .section { margin-top: 16px; }
  .section-title { font-size: 22px; font-weight: 300; color: var(--ink); }
  .section-line {
    font-size: 14px; font-weight: 300; color: var(--white);
    letter-spacing: 0.5px; margin-top: 3px; padding-left: 14px; position: relative;
  }
  .section-line.bullet::before {
    content: ""; position: absolute; left: 2px; top: 3px;
    border-left: 6px solid var(--ink); border-top: 4px solid transparent; border-bottom: 4px solid transparent;
  }
  .divider { height: 1px; background: var(--panel-line); margin-top: 12px; margin-left: -18px; }
</style>
</head>
<body>

<section class="card card--front" aria-label="Card front">
  <div class="front-photo" role="img" aria-label="Photo of a green farm field with a wooden fence under a blue sky"></div>
  <div class="front-band">
    <p class="front-name">Dana Kessler</p>
    <p class="front-contact">787 555 0190 / dkessler@quillpost.example</p>
  </div>
  <p class="front-company">Brosmere Holdings Inc</p>
</section>

<section class="card card--back" aria-label="Card back">
  <div class="back-photo-left" role="img" aria-label="Photo of a field at dusk"></div>
  <div class="icon-column">
    <svg class="icon icon--phone" viewBox="0 0 34 30" aria-hidden="true">
      <path d="M4 10c0-4 6-6 13-6s13 2 13 6v2h-7v-3h-12v3H4z"/>
      <rect x="8" y="13" width="18" height="13" rx="2"/>
    </svg>
    <svg class="icon icon--mail" viewBox="0 0 34 30" aria-hidden="true">
      <path d="M3 6h28v18H3z"/>
      <path d="M3 6l14 11L31 6" fill="none" stroke="#e8e8e8" stroke-width="2"/>
    </svg>
    <svg class="icon icon--home" viewBox="0 0 34 30" aria-hidden="true">
      <path d="M17 3L2 15h4v12h8v-8h6v8h8V15h4z"/>
    </svg>
  </div>
  <div class="info-panel-wide">
    <h1 class="company-title">Brosmere Holdings Inc</h1>
    <div class="section">
      <p class="section-title">Phone:</p>
      <p class="section-line bullet">Office: (608) 555-0417</p>
      <p class="section-line bullet">Fax: (608) 555-0283</p>
      <div class="divider"></div>
    </div>
    <div class="section">
      <p class="section-title">Email</p>
      <p class="section-line bullet">brosmereoffice@quillpost.example</p>
      <div class="divider"></div>
    </div>
    <div class="section">
      <p class="section-title">Address</p>
      <p class="section-line bullet">1187 Larkin Rd. Pell Hollow,</p>
      <p class="section-line">WI 54872</p>
    </div>
  </div>
  <div class="back-photo-right" role="img" aria-label="Photo of a tree on the edge of a field under an evening sky"></div>
</section>

</body>
</html>
```